Business Card Design

We are a manufacturing and distribution company with most of our customer base being supermarkets. We have established brand guidelines that are attached.

```html
<!DOCTYPE html>
<html lang="en">
<head>
<meta charset="utf-8">
<title>Corvane Business Card</title>
<link rel="stylesheet" href="https://fonts.googleapis.com/css2?family=Montserrat:wght@700;800&family=Open+Sans:wght@400&display=swap">
<style>
  :root {
    --stage: #2b2b2d;
    --card: #0c0c0d;
    --card-edge: #1a1a1b;
    --white: #ffffff;
    --red: #e3202b;
    --blue: #1b6fb6;
    --grey-text: #d8d8d8;
    --rule: #8a8a8a;
    --pattern-dark: #0a0a0b;
    --pattern-light: #3a3a3c;
  }
  * { box-sizing: border-box; margin: 0; padding: 0; }
  html, body { width: 1200px; height: 1108px; overflow: hidden; }
  body { background: var(--stage); position: relative; font-family: "Open Sans", sans-serif; }

  .card {
    position: absolute;
    top: 164px;
    width: 440px;
    height: 780px;
    border-radius: 26px;
    background: var(--card);
    border: 1px solid var(--card-edge);
    overflow: hidden;
  }
  .card--front { left: 140px; }
  .card--back { left: 620px; }

  /* front */
  .front-pattern {
    position: absolute; inset: 0;
    background: linear-gradient(160deg, var(--pattern-dark) 0%, var(--pattern-dark) 35%, var(--pattern-light) 100%);
  }
  .front-brand {
    position: absolute;
    left: 44px; top: 560px;
    display: flex; align-items: center; gap: 14px;
  }
  .brand-square { width: 30px; height: 30px; background: var(--red); }
  .brand-name {
    font-family: "Montserrat", sans-serif;
    font-weight: 800;
    color: var(--white);
    letter-spacing: 2px;
  }
  .front-brand .brand-name { font-size: 40px; }

  /* back */
  .back-brand {
    position: absolute; top: 232px; left: 0; right: 0;
    display: flex; justify-content: center; align-items: center; gap: 16px;
  }
  .back-brand .brand-name { font-size: 48px; }
  .back-brand .brand-square { width: 38px; height: 38px; }

  .person { position: absolute; top: 340px; left: 0; right: 0; text-align: center; }
  .person-name {
    font-family: "Montserrat", sans-serif; font-weight: 800;
    color: var(--red); font-size: 34px; letter-spacing: 1px;
  }
  .person-role { color: var(--grey-text); font-size: 18px; margin-top: 2px; }

  .icon-row {
    position: absolute; top: 428px; left: 50px; right: 50px;
    display: flex; align-items: center; gap: 10px;
  }
  .icon-row .rule { flex: 1; height: 1px; background: var(--rule); }
  .icon {
    width: 36px; height: 36px; border-radius: 5px;
    background: var(--blue); display: flex; align-items: center; justify-content: center;
  }

  .contacts {
    position: absolute; top: 486px; left: 0; right: 0; text-align: center;
    color: var(--grey-text); font-size: 20px; line-height: 30px;
  }
  .divider { position: absolute; top: 590px; left: 50px; right: 50px; height: 1px; background: var(--rule); }
  .address {
    position: absolute; top: 608px; left: 0; right: 0; text-align: center;
    color: var(--grey-text); font-size: 20px; line-height: 28px;
  }
</style>
</head>
<body>
  <section class="card card--front">
    <div class="front-pattern" role="img" aria-label="Repeating tonal brand pattern fading from black to dark grey"></div>
    <div class="front-brand">
      <span class="brand-square"></span>
      <span class="brand-name">CORVANE</span>
    </div>
  </section>

  <section class="card card--back">
    <div class="back-brand">
      <span class="brand-square"></span>
      <span class="brand-name">CORVANE</span>
    </div>

    <div class="person">
      <div class="person-name">DANA REYES</div>
      <div class="person-role">Manager</div>
    </div>

    <div class="icon-row">
      <span class="rule"></span>
      <span class="icon" aria-label="Phone">
        <svg width="20" height="20" viewBox="0 0 24 24"><path fill="#fff" d="M6.6 10.8c1.4 2.8 3.8 5.1 6.6 6.6l2.2-2.2c.3-.3.7-.4 1-.2 1.1.4 2.3.6 3.6.6.6 0 1 .4 1 1V20c0 .6-.4 1-1 1C10.6 21 3 13.4 3 4c0-.6.4-1 1-1h3.5c.6 0 1 .4 1 1 0 1.3.2 2.5.6 3.6.1.3 0 .7-.2 1l-2.3 2.2z"/></svg>
      </span>
      <span class="icon" aria-label="Email">
        <svg width="22" height="16" viewBox="0 0 22 16"><rect x="1" y="1" width="20" height="14" fill="#fff"/><path d="M1 1l10 8 10-8" fill="none" stroke="#1b6fb6" stroke-width="1.6"/></svg>
      </span>
      <span class="icon" aria-label="Website">
        <svg width="20" height="20" viewBox="0 0 20 20" fill="none" stroke="#fff" stroke-width="1.5"><circle cx="10" cy="10" r="8"/><ellipse cx="10" cy="10" rx="3.5" ry="8"/><path d="M2 10h16M3.5 5.5h13M3.5 14.5h13"/></svg>
      </span>
      <span class="rule"></span>
    </div>

    <div class="contacts">
      <div>(555) 014-2739</div>
      <div>info@corvanemail.com</div>
      <div>www.corvane.com</div>
    </div>

    <div class="divider"></div>

    <div class="address">
      <div>4821 Harbor Mill Rd. Suite 210</div>
      <div>Austin, TX 0000</div>
    </div>
  </section>
</body>
</html>
```